Etiketten-Design für Getränke
Zielgruppe
Wir sind ein Restaurant und starten jetzt mit der Herstellung von eigenen Getränken wie z.B. Whisky, Gin, Rum, Weine, Liköre etc. Die erste Linie des Whiksy haben wir selbst entworfen möchten aber mehr Professionalität einbringen.
Aufgabenstellung
Beiliegend die beiden Flaschen welche bedruckt/beklebt werden (mit Flaschenbezeichnung) und unser LOGO als PSD.
Stichworte: Regional, Qualität, Beste Zutaten, keine Zusatzstoffe
Bezeichnungen: Silberfalter Whisky / Silberfalter Gin
Wichtig: Wiederkennungswert schaffen (Es sollen in Zukunft auch Weine, Liköre etc. produziert werden)
Infos Gin:
- 65 verschiedenen Botanicals
- Neben Blutorangen, Zitronen und Limetten, zeigt auch der Duft von Ingwer, Zitronengras und Kaffirlimettenblätter als Zitrusensemble das Facettenreichtum des Gins. Das Aromaspiel verändert sich nach etwas Zeit im Glas sehr deutlich. Dann zeigen sich starke Aromakomponenten wie Kardamom, Koriander oder Piment. Der Gin zeichnet sich aus durch seine Lebendigkeit
- 42%vol
- 500ml
Infos Whisky:
- 8 Jahre gereift
- Zur Vergärung unseres Whiskys verwenden wir eigens gezüchtete Frischhefe mit besonderen Fähigkeiten zur Bildung von sehr fruchtigen Gäraromen. Die Weichheit bekommt er durch die dreifache Destillation. Auch bei der Wahl unserer Gerste setzen wir auf unsere Region. Der Grund für diesen starken regionalen Bezug ist, dass wir versuchen unserem Whisky die größtmögliche Portion an Terroir zu verleihen. Bei der anschließenden Fasslagerung setzen wir auf hochwertige Fässer. Zuerst neue amerikanische Weißeiche mit anschließendem Sherry- und Cognacfass finish.
Tradition und Moderne verschmelzen zu einem unverwechselbaren Whisky, mit weichem, fruchtigen femininen Geschmack und wildem, maskulinen Charakter.
- Single Malt Whisky
- Geruch & Geschmack: Der Whisky zeichnet sich aus durch intensive, weiche Aromen nach Vanille und süßen Früchten, mit einem ungewöhnlich weichen und sanften Abgang mit einem Hauch von dunkler Schokolade.
Folgende obligatorischen Angaben sind Pflicht:
- Adresse 'Silberfalter / Lindenhang 7 / 76351 Linkenheim-Hochstetten'
- Losnummer z.B. L0121..

```html
<!DOCTYPE html>
<html lang="de">
<head>
<meta charset="utf-8">
<title>Silberfalter – Etiketten</title>
<link rel="stylesheet" href="https://fonts.googleapis.com/css2?family=Josefin+Sans:wght@400;600&family=Great+Vibes&family=Cormorant+Garamond:wght@500&family=Roboto+Condensed:wght@400&display=swap">
<style>
  :root {
    --bg-top: #ececec;
    --bg-bottom: #f3f3f3;
    --label-dark: #111315;
    --label-deep: #08090a;
    --gold: #c9a23f;
    --gold-soft: #8c7331;
    --ink-light: #f4f4f4;
    --ink-muted: #b9bcbf;
    --ornament: #2b2e31;
  }
  html, body {
    margin: 0;
    width: 1200px;
    height: 2400px;
    overflow: hidden;
  }
  body {
    position: relative;
    background: linear-gradient(180deg, var(--bg-top) 0%, #e9e9e9 68%, var(--bg-bottom) 68%, #fafafa 100%);
    font-family: "Josefin Sans", sans-serif;
  }

  /* ---------- label base ---------- */
  .label {
    position: absolute;
    box-sizing: border-box;
    overflow: hidden;
    background: linear-gradient(180deg, var(--label-dark), var(--label-deep));
    border-radius: 50% 50% 0 0 / 1.3em 1.3em 0 0;
    color: var(--ink-light);
    display: flex;
    flex-direction: column;
    align-items: center;
    text-align: center;
    padding: 0.9em 0 1.3em;
    line-height: 1.2;
  }
  .label--no-footer { padding-bottom: 0.6em; padding-top: 0.7em; }
  .label::before {
    content: "";
    position: absolute;
    inset: 0.3em;
    border: 1px solid var(--gold-soft);
    border-radius: 50% 50% 0 0 / 1.1em 1.1em 0 0;
    pointer-events: none;
  }
  .label__ornament {
    position: absolute;
    width: 2.3em;
    height: 0.9em;
    background: var(--ornament);
    border-radius: 0.45em;
  }
  .label__ornament--tl { left: 0.9em; top: 1.6em; }
  .label__ornament--tr { right: 0.9em; top: 1.6em; }
  .label__ornament--bl { left: 0.9em; bottom: 4.2em; }
  .label__ornament--br { right: 0.9em; bottom: 4.2em; }
  .label__badge {
    flex: none;
    width: 1.9em;
    height: 1.9em;
    border-radius: 50%;
    background: var(--label-deep);
    border: 1px solid var(--gold);
    box-sizing: border-box;
  }
  .label__brand {
    color: var(--gold);
    font-size: 0.85em;
    letter-spacing: 0.04em;
    margin-top: 0.5em;
  }
  .label__title {
    font-size: 1.9em;
    letter-spacing: 0.06em;
    line-height: 1;
    margin-top: 0.45em;
  }
  .label__rule {
    flex: none;
    width: 2em;
    height: 1px;
    background: var(--gold);
    margin: 0.5em auto 0.35em;
  }
  .label__script {
    font-family: "Great Vibes", cursive;
    font-size: 1.05em;
  }
  .label__age {
    font-size: 1.1em;
    line-height: 1;
    margin-top: 0.55em;
  }
  .label__age-caption {
    font-size: 0.48em;
    font-weight: 600;
    letter-spacing: 0.06em;
  }
  .label__note {
    font-size: 0.45em;
    letter-spacing: 0.08em;
    line-height: 1.35;
    margin-top: 0.4em;
  }
  .label__bottom {
    margin-top: auto;
    padding-top: 0.4em;
    display: flex;
    flex-direction: column;
    align-items: center;
  }
  .label__tagline {
    font-size: 0.34em;
    font-weight: 600;
    letter-spacing: 0.08em;
    line-height: 1.3;
  }
  .label__divider-ornament {
    width: 2.6em;
    height: 0.5em;
    background: var(--gold-soft);
    border-radius: 0.25em;
    margin-top: 0.25em;
  }
  .label__footer {
    position: absolute;
    left: 0.75em;
    right: 0.75em;
    bottom: 0.6em;
    display: flex;
    justify-content: space-between;
    font-family: "Cormorant Garamond", serif;
    font-size: 0.6em;
    font-weight: 500;
    line-height: 1;
  }
  .label__footer small { font-size: 0.7em; letter-spacing: 0.04em; }

  /* ---------- back label ---------- */
  .label--back { padding-top: 1.1em; }
  .label--back .label__ornament--tl,
  .label--back .label__ornament--tr { top: 1.1em; width: 1.8em; height: 0.7em; }
  .label--back .label__badge { width: 1.1em; height: 1.1em; }
  .label--back .label__brand { font-size: 0.6em; margin-top: 0.4em; }
  .back__title {
    font-size: 0.62em;
    letter-spacing: 0.14em;
    margin-top: 1.4em;
  }
  .back__subtitle {
    color: var(--gold);
    font-family: "Roboto Condensed", sans-serif;
    font-size: 0.45em;
  }
  .back__body {
    font-family: "Roboto Condensed", sans-serif;
    font-size: 0.38em;
    line-height: 1.3;
    color: var(--ink-muted);
    padding: 0 2.4em;
    margin-top: 1.6em;
  }
  .back__body p { margin: 0 0 0.9em; }
  .back__ornament {
    flex: none;
    width: 2.4em;
    height: 0.35em;
    background: var(--ornament);
    border-radius: 0.2em;
    margin: 0.2em auto 0.5em;
  }
  .back__maker { font-size: 0.38em; letter-spacing: 0.14em; }
  .back__address {
    font-family: "Roboto Condensed", sans-serif;
    font-size: 0.36em;
    color: var(--ink-muted);
  }
  .back__lot {
    font-family: "Roboto Condensed", sans-serif;
    font-size: 0.36em;
    margin-top: 1.4em;
  }

  /* ---------- placements ---------- */
  .whisky-front   { left: 513px; top: 387px;  width: 160px; height: 225px; font-size: 16px; }
  .whisky-back    { left: 807px; top: 403px;  width: 136px; height: 211px; font-size: 13.6px; }
  .gin-front      { left: 500px; top: 1155px; width: 176px; height: 272px; font-size: 17.6px; }
  .gin-back       { left: 793px; top: 1185px; width: 136px; height: 211px; font-size: 13.6px; }
  .whisky-dark    { left: 209px; top: 2012px; width: 109px; height: 146px; font-size: 10.6px; }
  .whisky-amber   { left: 409px; top: 2062px; width: 120px; height: 169px; font-size: 12px; }
  .pear-liqueur   { left: 731px; top: 1973px; width: 105px; height: 210px; font-size: 10.5px; }
  .liqueur-small  { left: 961px; top: 2025px; width: 83px;  height: 117px; font-size: 8.3px; }

  .gin-front .label__title { font-size: 2.1em; letter-spacing: 0.2em; margin-top: 0.5em; }
  .gin-front .label__note { font-family: "Roboto Condensed", sans-serif; font-size: 0.42em; letter-spacing: 0.1em; }
  .pear-liqueur .label__ornament--tl,
  .pear-liqueur .label__ornament--tr { top: 2.8em; }
  .pear-liqueur .label__badge { margin-top: 1.4em; }
  .pear-liqueur .label__note { font-family: "Roboto Condensed", sans-serif; font-size: 0.42em; letter-spacing: 0.04em; margin-top: 1.2em; }
  .liqueur-small .label__script { margin-top: 0.4em; }
</style>
</head>
<body>

<!-- Whisky, front -->
<section class="label whisky-front" aria-label="Whisky Etikett vorne">
  <div class="label__ornament label__ornament--tl" role="img" aria-label="Zierranke"></div>
  <div class="label__ornament label__ornament--tr" role="img" aria-label="Zierranke"></div>
  <div class="label__ornament label__ornament--bl" role="img" aria-label="Zierranke"></div>
  <div class="label__ornament label__ornament--br" role="img" aria-label="Zierranke"></div>
  <div class="label__badge"></div>
  <div class="label__brand">Silberfalter</div>
  <div class="label__title">WHISKY</div>
  <div class="label__rule"></div>
  <div class="label__script">Single Malt</div>
  <div class="label__age">8</div>
  <div class="label__age-caption">YEARS OLD</div>
  <div class="label__bottom">
    <div class="label__tagline">WEICH &amp; INTENSIV</div>
    <div class="label__divider-ornament" role="img" aria-label="Goldenes Zierornament"></div>
  </div>
  <div class="label__footer"><span>42% <small>VOL</small></span><span>500 <small>ML</small></span></div>
</section>

<!-- Whisky, back -->
<section class="label label--back whisky-back" aria-label="Whisky Etikett hinten">
  <div class="label__ornament label__ornament--tl" role="img" aria-label="Zierranke"></div>
  <div class="label__ornament label__ornament--tr" role="img" aria-label="Zierranke"></div>
  <div class="label__badge"></div>
  <div class="label__brand">Silberfalter</div>
  <div class="back__title">WHISKY</div>
  <div class="back__subtitle">Single Malt – 8 Jahre gereift</div>
  <div class="back__body">
    <p>Regionale Gerste, vergoren durch eigens gezüchtete Frischhefe, dreifach destilliert für seine Weichheit und seinen Geschmack.</p>
    <p>Gelagert in amerikanischer Weißeiche, vollendet im Sherry- und Cognacfass.</p>
    <p>Tradition und Moderne verschmelzen zu einem weichen, fruchtigen Whisky mit wildem Charakter.</p>
  </div>
  <div class="back__ornament" role="img" aria-label="Zierlinie"></div>
  <div class="back__maker">SILBERFALTER</div>
  <div class="back__address">Lindenhang 7 · 76351 Linkenheim-Hochstetten</div>
  <div class="back__lot">L0121</div>
</section>

<!-- Gin, front -->
<section class="label gin-front" aria-label="Gin Etikett vorne">
  <div class="label__ornament label__ornament--tl" role="img" aria-label="Zierranke"></div>
  <div class="label__ornament label__ornament--tr" role="img" aria-label="Zierranke"></div>
  <div class="label__ornament label__ornament--bl" role="img" aria-label="Zierranke"></div>
  <div class="label__ornament label__ornament--br" role="img" aria-label="Zierranke"></div>
  <div class="label__badge"></div>
  <div class="label__brand">Silberfalter</div>
  <div class="label__title">GIN</div>
  <div class="label__rule"></div>
  <div class="label__script">Komposition</div>
  <div class="label__note">aus 65 verschiedenen<br>Botanicals</div>
  <div class="label__bottom">
    <div class="label__tagline">LUXURY EDITION</div>
    <div class="label__divider-ornament" role="img" aria-label="Goldenes Zierornament"></div>
  </div>
  <div class="label__footer"><span>42% <small>VOL</small></span><span>500 <small>ML</small></span></div>
</section>

<!-- Gin, back -->
<section class="label label--back gin-back" aria-label="Gin Etikett hinten">
  <div class="label__ornament label__ornament--tl" role="img" aria-label="Zierranke"></div>
  <div class="label__ornament label__ornament--tr" role="img" aria-label="Zierranke"></div>
  <div class="label__badge"></div>
  <div class="label__brand">Silberfalter</div>
  <div class="back__title">GIN KOMPOSITION</div>
  <div class="back__subtitle">aus 65 verschiedenen Botanicals</div>
  <div class="back__body">
    <p>Ein facettenreiches Zitrus-Ensemble aus Blutorangen, Zitronen, Limetten, Ingwer, Zitronengras und Kaffirlimettenblättern.</p>
    <p>Nach einiger Zeit im Glas zeigen sich Kardamom, Koriander und Piment.</p>
    <p>Unser Silberfalter Gin zeichnet sich durch seine Lebendigkeit aus.</p>
  </div>
  <div class="back__ornament" role="img" aria-label="Zierlinie"></div>
  <div class="back__maker">SILBERFALTER</div>
  <div class="back__address">Lindenhang 7 · 76351 Linkenheim-Hochstetten</div>
  <div class="back__lot">L0121</div>
</section>

<!-- Whisky, dark bottle variant -->
<section class="label label--no-footer whisky-dark" aria-label="Whisky Etikett, Variante dunkel">
  <div class="label__ornament label__ornament--tl" role="img" aria-label="Zierranke"></div>
  <div class="label__ornament label__ornament--tr" role="img" aria-label="Zierranke"></div>
  <div class="label__badge"></div>
  <div class="label__brand">Silberfalter</div>
  <div class="label__title">WHISKY</div>
  <div class="label__rule"></div>
  <div class="label__script">Single Malt</div>
  <div class="label__age">8</div>
  <div class="label__age-caption">YEARS OLD</div>
  <div class="label__bottom">
    <div class="label__tagline">WEICH &amp; INTENSIV</div>
    <div class="label__divider-ornament" role="img" aria-label="Goldenes Zierornament"></div>
  </div>
</section>

<!-- Whisky, amber bottle variant -->
<section class="label label--no-footer whisky-amber" aria-label="Whisky Etikett, Variante bernstein">
  <div class="label__ornament label__ornament--tl" role="img" aria-label="Zierranke"></div>
  <div class="label__ornament label__ornament--tr" role="img" aria-label="Zierranke"></div>
  <div class="label__badge"></div>
  <div class="label__brand">Silberfalter</div>
  <div class="label__title">WHISKY</div>
  <div class="label__rule"></div>
  <div class="label__script">Single Malt</div>
  <div class="label__age">8</div>
  <div class="label__age-caption">YEARS OLD</div>
  <div class="label__bottom">
    <div class="label__tagline">WEICH &amp; INTENSIV</div>
    <div class="label__divider-ornament" role="img" aria-label="Goldenes Zierornament"></div>
  </div>
</section>

<!-- Pear liqueur -->
<section class="label pear-liqueur" aria-label="Birnenlikör Etikett">
  <div class="label__ornament label__ornament--tl" role="img" aria-label="Zierranke"></div>
  <div class="label__ornament label__ornament--tr" role="img" aria-label="Zierranke"></div>
  <div class="label__ornament label__ornament--bl" role="img" aria-label="Zierranke"></div>
  <div class="label__ornament label__ornament--br" role="img" aria-label="Zierranke"></div>
  <div class="label__badge"></div>
  <div class="label__brand">Silberfalter</div>
  <div class="label__title">BIRNE</div>
  <div class="label__rule"></div>
  <div class="label__script">Likör</div>
  <div class="label__note">Das Beste der<br>Williams Christ Birne</div>
  <div class="label__bottom">
    <div class="label__tagline">LUXURY EDITION</div>
    <div class="label__divider-ornament" role="img" aria-label="Goldenes Zierornament"></div>
  </div>
  <div class="label__footer"><span>42% <small>VOL</small></span><span>500 <small>ML</small></span></div>
</section>

<!-- Small liqueur -->
<section class="label liqueur-small" aria-label="Likör Etikett">
  <div class="label__badge"></div>
  <div class="label__brand">Silberfalter</div>
  <div class="label__title">LIQUER</div>
  <div class="label__script">Taste it</div>
  <div class="label__bottom">
    <div class="label__tagline">LIMITED EDITION</div>
    <div class="label__divider-ornament" role="img" aria-label="Goldenes Zierornament"></div>
  </div>
  <div class="label__footer"><span>42% <small>VOL</small></span><span>500 <small>ML</small></span></div>
</section>

</body>
</html>
```